New web design for a service provider in the medical field

We are looking for a new design for our website. We are a company that repairs and sells medical endoscopes. Our customers include doctors and hospitals. Our current website can be found at https://lumenfix.example/en/lumenfix-english.
We need a new web design (without programming) for the following 3 pages:
-Startpage https://lumenfix.example/en/lumenfix-english/
-Used endoscopes https://lumenfix.example/en/used-endoscopes/
-Purchase https://lumenfix.example/en/purchase/
The design should be modern and stylish.
The blue color of the logo should be reflected on the page, but not too intrusive.
I have uploaded the images from the header. If more images are needed, let me know and I will upload them.

Target Market(s)
Doctors and hospitals

```html
<!DOCTYPE html>
<html lang="en">
<head>
<meta charset="utf-8">
<title>LumenFix – Endoscope Repair &amp; Sales</title>
<link href="https://fonts.googleapis.com/css2?family=Poppins:wght@400;500;600;700;800&family=Archivo:wght@800;900&display=swap" rel="stylesheet">
<style>
:root{
  --blue:#1ba3dc;
  --blue-dark:#1690c4;
  --navy:#1e3550;
  --text:#5b6470;
  --muted:#8a929c;
  --footer:#283d53;
  --footer-text:#c9d3de;
  --grey-bg:#eef0f2;
  --white:#ffffff;
  --brand-a:#0f4c8c;
  --brand-b:#e8322a;
  --brand-c:#0b0b0b;
}
*{margin:0;padding:0;box-sizing:border-box}
html,body{width:1200px;height:4317px;overflow:hidden;background:var(--white)}
body{position:relative;font-family:"Poppins",sans-serif;color:var(--text)}
.abs{position:absolute}
.display{font-family:"Archivo","Poppins",sans-serif;font-weight:900;letter-spacing:.5px}

/* top bar */
.topbar{left:0;top:0;width:1200px;height:37px}
.topbar-links{top:0;height:37px;display:flex;align-items:center;font-size:11.5px;color:var(--white)}
.topbar-links span{margin:0 8px}

/* header */
.logo{left:92px;top:42px;display:flex;align-items:center;gap:10px;font-weight:700;font-size:22px;color:var(--navy)}
.logo .dot{width:16px;height:16px;border-radius:50%;background:var(--blue)}
.nav{top:76px;left:0;width:1200px;height:18px;font-size:11.5px;font-weight:500;color:var(--navy)}
.nav a{position:absolute;text-decoration:none;color:inherit;white-space:nowrap}
.nav a.active{color:var(--blue)}

/* hero */
.hero{left:0;top:125px;width:1200px;height:700px;overflow:hidden}
.hero-photo{position:absolute;inset:0;background:linear-gradient(100deg,#a9aeb3 0%,#c9cdd1 45%,#e9eaec 75%,#dcdee1 100%)}
.hero-kicker{left:86px;top:275px;font-size:19px;font-weight:700;color:var(--white)}
.hero-title{left:84px;top:302px;font-size:76px;line-height:.98;color:var(--white)}
.btn{display:flex;align-items:center;justify-content:center;border-radius:30px;font-size:12px;font-weight:700;text-transform:uppercase;text-decoration:none}
.btn-blue{background:var(--blue);color:var(--white)}
.btn-white{background:var(--white);color:var(--navy)}

/* intro */
.section-kicker{left:0;width:1200px;text-align:center;font-size:12.5px;color:var(--muted);letter-spacing:.5px}
.section-title{left:0;width:1200px;text-align:center;color:var(--navy);font-size:36px}
.intro-text{left:300px;width:600px;text-align:center;font-size:14px;line-height:24px}

/* repairs */
.repairs-title{left:678px;top:1138px;font-size:35px;line-height:36px;color:var(--navy)}
.repairs-sub{left:679px;top:1222px;font-size:12.5px;font-weight:600;color:var(--navy);line-height:20px}
.repairs-text{left:679px;top:1270px;width:420px;font-size:14px;line-height:24px}

/* service cards */
.band-blue{left:0;top:1897px;width:1200px;height:366px;background:var(--blue)}
.card{top:1617px;width:278px;height:335px;background:var(--white);border-radius:8px;box-shadow:0 10px 28px rgba(30,53,80,.12);text-align:center}
.card svg{margin-top:36px}
.card h3{margin-top:20px;font-size:13px;font-weight:700;color:var(--navy);line-height:20px}
.card p{margin:14px 26px 0;font-size:12.5px;line-height:20.5px;color:var(--muted)}
.card .card-link{position:absolute;left:0;right:0;bottom:0;height:60px;border-top:1px solid #e4e8ec;display:flex;align-items:center;justify-content:center;font-size:12px;font-weight:700;color:var(--blue)}

.faulty-title{left:0;width:1200px;top:2036px;text-align:center;font-size:54px;color:var(--white)}
.faulty-sub{left:0;width:1200px;top:2106px;text-align:center;font-size:16.5px;font-weight:600;color:var(--white)}

/* cause */
.cause-title{left:633px;top:2385px;font-size:35px;line-height:40px;color:var(--navy)}
.check-list{left:633px;top:2487px;list-style:none;width:520px}
.check-list li{position:relative;padding-left:19px;height:58.6px}
.check-list li svg{position:absolute;left:0;top:4px}
.check-list strong{display:block;font-size:13px;font-weight:700;color:var(--navy);line-height:18px}
.check-list span{display:block;font-size:12.5px;line-height:20px;color:var(--muted)}

/* decision */
.decision-title{left:0;top:2946px;width:1200px;text-align:center;font-size:37px;line-height:44px;color:var(--navy)}
.feature{width:440px;padding-left:62px}
.feature svg{position:absolute;left:0;top:2px}
.feature h4{font-size:13px;font-weight:700;color:var(--navy);line-height:18px}
.feature p{margin-top:6px;font-size:12.5px;line-height:21px;color:var(--muted)}

.brand-circle{width:178px;height:178px;border-radius:50%;display:flex;align-items:center;justify-content:center;color:var(--white);font-size:25px}

/* cta */
.cta{left:176px;top:3667px;width:848px;height:163px;border-radius:82px;background:var(--blue);box-shadow:0 18px 36px rgba(27,163,220,.25);z-index:3}
.cta-title{left:119px;top:36px;font-size:50px;line-height:48px;color:var(--white)}

/* footer */
.footer-head{font-size:17px;font-weight:700;color:var(--white)}
.footer-list{list-style:none;font-size:12.5px;color:var(--footer-text)}
.footer-list li{height:31px;display:flex;align-items:center;gap:8px}
.contact-item{font-size:12.5px;line-height:18px;color:var(--footer-text);padding-left:23px;position:relative}
.contact-item svg{position:absolute;left:0;top:2px}
.news-input{left:850px;top:4048px;width:259px;height:45px;background:var(--white);border-radius:23px;display:flex;align-items:center;padding:0 18px;font-size:12px;color:#55606b;gap:8px}
.social{width:34px;height:34px;border-radius:50%;background:#3a5069}
.copyright{left:0;top:4278px;width:1200px;text-align:center;font-size:12.5px;font-weight:600;color:var(--white)}
</style>
</head>
<body>

<!-- top bar -->
<svg class="abs topbar" viewBox="0 0 1200 37" aria-hidden="true"><polygon points="494,0 1200,0 1200,37 474,37" fill="var(--blue)"/></svg>
<div class="abs topbar-links" style="left:513px">Cause the outcome matters</div>
<div class="abs topbar-links" style="left:740px">Pick-up order<span>|</span>About us<span>|</span>Contact us</div>
<div class="abs topbar-links" style="left:1055px">English&nbsp;&#8964;</div>

<!-- header -->
<div class="abs logo"><span class="dot"></span>LumenFix</div>
<nav class="abs nav">
  <a class="active" style="left:315px">HOME</a>
  <a style="left:384px">ENDOSCOPE REPAIR</a>
  <a style="left:536px">USED ENDOSCOPES &#8964;</a>
  <a style="left:685px">ENDOSCOPY SYSTEMS</a>
  <a style="left:851px">ENDOSCOPY ACCESSORIES &#8964;</a>
  <a style="left:1047px">PURCHASE</a>
</nav>

<!-- hero -->
<section class="abs hero">
  <div class="hero-photo" role="img" aria-label="Photo of a flexible endoscope control body in a white holder"></div>
  <svg class="abs" style="left:0;top:0" width="1200" height="700" viewBox="0 0 1200 700" aria-hidden="true">
    <path d="M0,680 C170,520 420,470 620,520 C820,570 980,690 1200,640 L1200,700 L0,700 Z" fill="#e2e5e8"/>
    <path d="M0,695 C180,545 420,500 620,545 C830,592 990,705 1200,665 L1200,700 L0,700 Z" fill="var(--white)"/>
  </svg>
</section>
<div class="abs hero-kicker">PUT YOUR ENDOSCOPE IN</div>
<div class="abs hero-title display">RELIABLE<br>HANDS!</div>
<a class="abs btn btn-blue" style="left:89px;top:482px;width:146px;height:42px">Contact us</a>

<!-- intro -->
<div class="abs section-kicker" style="top:852px">YOUR FUTURE</div>
<h2 class="abs section-title display" style="top:872px">OUR SERVICE</h2>
<p class="abs intro-text" style="top:930px">LumenFix GmbH is specialised in the repair and sale of Oryntal, Pendrix and Fulcron flexible medical endoscopes. As a service-oriented company, we are at your side with our knowledge and skills!</p>

<!-- repairs -->
<svg class="abs" style="left:0;top:1045px" width="600" height="500" viewBox="0 0 600 500" role="img" aria-label="Photo of an endoscope control body and insertion tube on a white surface">
  <defs>
    <linearGradient id="repairPhoto" x1="0" y1="0" x2="1" y2="1">
      <stop offset="0" stop-color="#d9dcdf"/><stop offset=".55" stop-color="#b9bec3"/><stop offset="1" stop-color="#e7e9eb"/>
    </linearGradient>
  </defs>
  <path d="M300,10 C420,-10 560,40 580,140 C600,250 520,360 470,420 L330,420 Z" fill="#cdeaf7"/>
  <path d="M0,70 C120,40 260,15 370,30 C520,55 560,200 540,310 C520,420 470,490 420,490 C330,490 270,420 180,400 C120,387 50,395 0,400 Z" fill="url(#repairPhoto)"/>
</svg>
<h2 class="abs repairs-title display">ENDOSCOPE<br>REPAIRS</h2>
<p class="abs repairs-sub">AND SECOND HAND ENDOSCOPES FROM LUMENFIX<br>CAUSE THE OUTCOME MATTERS!</p>
<p class="abs repairs-text">LumenFix is a privileged partner for the start-up facility or optimisation of existing healthcare facilities, doctor's offices and hospitals. The quality and reliability of our products and our offered service are our best advertisement!</p>
<a class="abs btn btn-blue" style="left:679px;top:1417px;width:127px;height:42px">Read more</a>

<!-- services -->
<div class="abs band-blue"></div>
<svg class="abs" style="left:800px;top:2030px" width="400" height="233" viewBox="0 0 400 233" role="img" aria-label="Photo of a blue-lit endoscope control head"><path d="M20,233 C60,150 140,80 260,40 C320,20 370,10 400,10 L400,233 Z" fill="#1590c4" opacity=".75"/></svg>

<div class="abs card" style="left:166px">
  <svg width="76" height="76" viewBox="0 0 76 76" fill="none" stroke="var(--navy)" stroke-width="2.2" stroke-linecap="round" stroke-linejoin="round" aria-hidden="true"><circle cx="30" cy="30" r="14"/><circle cx="30" cy="30" r="5"/><path d="M30,10v6M30,44v6M10,30h6M44,30h6M16,16l4,4M40,40l4,4M44,16l-4,4M16,44l4-4"/><path d="M44,44l20,20M58,22l-6,6 4,4 6-6M26,56l-8,8"/></svg>
  <h3>REPAIR ENDOSCOPE<br>REPAIR SERVICE</h3>
  <p>Manufacturer-independent we repair and maintain endoscopes, individual components...</p>
  <div class="card-link">REPAIR REQUEST</div>
</div>
<div class="abs card" style="left:461px">
  <svg width="76" height="76" viewBox="0 0 76 76" fill="none" stroke="var(--navy)" stroke-width="2.2" stroke-linejoin="round" aria-hidden="true"><path d="M8,10h26l30,30-24,24L8,32Z"/><circle cx="20" cy="22" r="4"/><path d="M34,48l16-16"/></svg>
  <h3>SALE USED<br>ENDOSCOPES</h3>
  <p>Our regular stock includes refurbished gastroscopes, coloscopes, bronchoscopes...</p>
  <div class="card-link">PURCHASE REQUEST</div>
</div>
<div class="abs card" style="left:756px">
  <svg width="76" height="76" viewBox="0 0 76 76" fill="none" stroke="var(--navy)" stroke-width="2.2" stroke-linecap="round" stroke-linejoin="round" aria-hidden="true"><path d="M8,22h8l8,32h34l6-24H22"/><circle cx="30" cy="64" r="4"/><circle cx="52" cy="64" r="4"/><circle cx="44" cy="16" r="9"/><path d="M44,11v10"/></svg>
  <h3>PURCHASE<br>USED ENDOSCOPES</h3>
  <p>We are very interested in buying your old endoscopes – even defective and dismantled!...</p>
  <div class="card-link">SELL DEVICE</div>
</div>

<h2 class="abs faulty-title display">FAULTY ENDOSCOPE?</h2>
<div class="abs faulty-sub">WE ENSURE QUICK AND SMOOTH REPAIRS!</div>
<a class="abs btn btn-white" style="left:516px;top:2147px;width:168px;height:42px">Pick-up order</a>

<!-- cause -->
<div class="abs" style="left:84px;top:2346px;width:494px;height:503px;background:radial-gradient(ellipse at 50% 50%,#eceef0 0%,#ffffff 70%)" role="img" aria-label="Photo of a coiled flexible endoscope with faint word ENDOSCOPE behind it"></div>
<h2 class="abs cause-title display">CAUSE THE<br>OUTCOME MATTERS!</h2>
<ul class="abs check-list">
  <li><svg width="11" height="11" viewBox="0 0 12 12"><circle cx="6" cy="6" r="6" fill="var(--blue)"/><path d="M3,6.2l2,2 4-4" stroke="#fff" stroke-width="1.5" fill="none"/></svg><strong>ONE COMPANY FOR EVERYONE</strong><span>We are a service provider for doctors and hospitals!</span></li>
  <li><svg width="11" height="11" viewBox="0 0 12 12"><circle cx="6" cy="6" r="6" fill="var(--blue)"/><path d="M3,6.2l2,2 4-4" stroke="#fff" stroke-width="1.5" fill="none"/></svg><strong>EXPERIENCE CHARACTERISES US</strong><span>Our team has many years of experience in the business field!</span></li>
  <li><svg width="11" height="11" viewBox="0 0 12 12"><circle cx="6" cy="6" r="6" fill="var(--blue)"/><path d="M3,6.2l2,2 4-4" stroke="#fff" stroke-width="1.5" fill="none"/></svg><strong>THE PRODUCT IS CLOSE TO OUR HEARTS</strong><span>We repair and sell second hand, flexible endoscopes!</span></li>
  <li><svg width="11" height="11" viewBox="0 0 12 12"><circle cx="6" cy="6" r="6" fill="var(--blue)"/><path d="M3,6.2l2,2 4-4" stroke="#fff" stroke-width="1.5" fill="none"/></svg><strong>GUARANTEED SERVICE</strong><span>You receive a six-month warranty on all repairs!</span></li>
  <li><svg width="11" height="11" viewBox="0 0 12 12"><circle cx="6" cy="6" r="6" fill="var(--blue)"/><path d="M3,6.2l2,2 4-4" stroke="#fff" stroke-width="1.5" fill="none"/></svg><strong>QUALITY NOT QUANTITY</strong><span>Reliability and durability instead of inferior replacements!</span></li>
  <li><svg width="11" height="11" viewBox="0 0 12 12"><circle cx="6" cy="6" r="6" fill="var(--blue)"/><path d="M3,6.2l2,2 4-4" stroke="#fff" stroke-width="1.5" fill="none"/></svg><strong>SERVICES FOR EVERYONE</strong><span>Our service includes the manufacturers Oryntal, Pendrix and Fulcron!</span></li>
</ul>

<!-- decision -->
<h2 class="abs decision-title display">LUMENFIX GMBH, YOUR<br>DECISION FOR YOUR FUTURE</h2>

<div class="abs feature" style="left:126px;top:3067px">
  <svg width="46" height="50" viewBox="0 0 46 50" fill="none" stroke="var(--navy)" stroke-width="2" aria-hidden="true"><circle cx="23" cy="28" r="18"/><path d="M18,4h10M23,4v6M23,28V18M23,28l7,5"/></svg>
  <h4>FAST REPAIRS</h4><p>Keep potential disruptions in your doctor's office or in your hospital at minimum as a result of optimized...</p>
</div>
<div class="abs feature" style="left:636px;top:3067px">
  <svg width="46" height="50" viewBox="0 0 46 50" fill="none" stroke="var(--navy)" stroke-width="2" aria-hidden="true"><path d="M14,4h24v40H14Z"/><path d="M20,14h12M20,22h12M20,30h8"/><circle cx="12" cy="36" r="9"/><path d="M8,36l3,3 5-6"/></svg>
  <h4>HIGHLY COST EFFICIENT</h4><p>Benefit from our first class recommendations &amp; implementation by our experienced staff...</p>
</div>
<div class="abs feature" style="left:126px;top:3170px">
  <svg width="46" height="50" viewBox="0 0 46 50" fill="none" stroke="var(--navy)" stroke-width="2" aria-hidden="true"><circle cx="26" cy="16" r="10"/><circle cx="26" cy="16" r="4"/><path d="M4,36h10l8,4h10l10-8M4,46h12l10,2 16-10"/></svg>
  <h4>ON-SITE SERVICE</h4><p>We will gladly pay you a visit to to carry out analysis and repairs on site. Due to our many years of experience...</p>
</div>
<div class="abs feature" style="left:636px;top:3170px">
  <svg width="46" height="50" viewBox="0 0 46 50" fill="none" stroke="var(--navy)" stroke-width="2" aria-hidden="true"><path d="M4,8h26v34H4Z"/><path d="M10,16h14M10,24h14M10,32h8"/><circle cx="32" cy="28" r="10"/><path d="M32,22v12"/></svg>
  <h4>LOAN EQUIPMENT SERVICE</h4><p>Use our service of high-quality loan devices during the downtime of your defective endoscope (limited to stock)</p>
</div>
<div class="abs feature" style="left:126px;top:3272px">
  <svg width="46" height="50" viewBox="0 0 46 50" fill="none" stroke="var(--navy)" stroke-width="2" aria-hidden="true"><path d="M4,6h30v40H4Z"/><path d="M10,14h18M10,22h14M10,30h10"/><path d="M40,10l-16,26-2,6 5-4 16-26Z"/></svg>
  <h4>WITHOUT A MAINTENANCE CONTRACT</h4><p>No subscription or other maintenance contract, but one-time and sustainable repair work</p>
</div>
<div class="abs feature" style="left:636px;top:3272px">
  <svg width="46" height="50" viewBox="0 0 46 50" fill="none" stroke="var(--navy)" stroke-width="2" aria-hidden="true"><circle cx="22" cy="18" r="15"/><circle cx="22" cy="18" r="9"/><path d="M13,30l-6,16 7-3 4 6 4-12M31,30l6,16-7-3-4 6-4-12"/></svg>
  <h4>FIRST CLASS SERVICE</h4><p>Our clients always come first!</p>
</div>

<div class="abs" style="left:980px;top:3285px;width:220px;height:218px;background:linear-gradient(150deg,rgba(255,255,255,0) 30%,#d5d8db 55%,rgba(255,255,255,0) 80%)" role="img" aria-label="Photo of two rigid endoscopes"></div>

<div class="abs brand-circle display" style="left:315px;top:3414px;background:var(--brand-a)">ORYNTAL</div>
<div class="abs brand-circle display" style="left:511px;top:3414px;background:var(--brand-b)">PENDRIX</div>
<div class="abs brand-circle display" style="left:709px;top:3414px;background:var(--brand-c)">FULCRON</div>

<!-- footer -->
<svg class="abs" style="left:0;top:3690px" width="1200" height="627" viewBox="0 0 1200 627" aria-hidden="true">
  <path d="M0,250 C250,60 520,10 800,40 C1000,62 1120,110 1200,160 L1200,627 L0,627 Z" fill="#e6e9ec"/>
  <path d="M0,310 C260,110 540,60 820,90 C1010,112 1130,160 1200,205 L1200,627 L0,627 Z" fill="var(--footer)"/>
  <line x1="0" y1="548" x2="1200" y2="548" stroke="#3b5068" stroke-width="1"/>
</svg>

<div class="abs cta">
  <div class="abs cta-title display">HOW CAN WE<br>HELP YOU?</div>
  <a class="abs btn btn-white" style="left:516px;top:60px;width:210px;height:42px;font-size:11.5px">Send us a message!</a>
</div>

<div class="abs" style="left:90px;top:4015px;display:flex;align-items:center;gap:12px;font-size:32px;font-weight:700;color:var(--white)"><span style="width:20px;height:20px;border-radius:50%;background:var(--blue)"></span>LumenFix</div>

<div class="abs footer-head" style="left:417px;top:3943px">QUICK LINKS</div>
<ul class="abs footer-list" style="left:417px;top:3987px">
  <li>&#8250; Informations</li><li>&#8250; About Us</li><li>&#8250; Contact Us</li><li>&#8250; TOS</li><li>&#8250; Copyrights</li><li>&#8250; Privacy Policy</li>
</ul>

<div class="abs footer-head" style="left:602px;top:3943px">CONTACT INFO</div>
<div class="abs contact-item" style="left:602px;top:3993px"><svg width="13" height="10" viewBox="0 0 13 10"><rect x=".5" y=".5" width="12" height="9" rx="1" fill="none" stroke="var(--blue)"/><path d="M.5,.8l6,4.5 6-4.5" fill="none" stroke="var(--blue)"/></svg>Email:<br>info@lumenfix.example</div>
<div class="abs contact-item" style="left:602px;top:4040px"><svg width="12" height="12" viewBox="0 0 12 12"><path d="M2,1l3,0 1,3-2,1c1,2 2,3 3,3l1-2 3,1 0,3c-6,0-9-3-9-9Z" fill="var(--blue)"/></svg>Phone:<br>+49 4000 555 120-0</div>
<div class="abs contact-item" style="left:602px;top:4087px"><svg width="11" height="14" viewBox="0 0 11 14"><path d="M5.5,14C2,9 0,7 0,5a5.5,5.5 0 0 1 11,0c0,2-2,4-5.5,9Z" fill="var(--blue)"/><circle cx="5.5" cy="5" r="2" fill="var(--footer)"/></svg>Location:<br>Lindenweg 12 20095<br>Musterstadt Germany</div>

<div class="abs footer-head" style="left:850px;top:3945px">NEWSLETTER</div>
<p class="abs" style="left:850px;top:3990px;width:230px;font-size:12px;line-height:18px;color:var(--footer-text)">Subscribe to our email address to get the latest news.</p>
<div class="abs news-input"><svg width="12" height="9" viewBox="0 0 12 9"><rect x=".5" y=".5" width="11" height="8" fill="none" stroke="#9aa3ad"/></svg>Enter Your Email...<svg style="margin-left:auto" width="14" height="14" viewBox="0 0 14 14"><path d="M1,6l12-5-5,12-2-5Z" fill="var(--blue)"/></svg></div>
<div class="abs social" style="left:850px;top:4126px"></div>
<div class="abs social" style="left:892px;top:4126px"></div>

<div class="abs" style="left:1129px;top:4228px;width:48px;height:48px;border-radius:50%;background:var(--blue);display:flex;align-items:center;justify-content:center"><svg width="14" height="16" viewBox="0 0 14 16"><path d="M7,15V2M2,7l5-5 5,5" fill="none" stroke="#fff" stroke-width="1.6"/></svg></div>
<div class="abs copyright">© 2022 LUMENFIX GMBH, ALL RIGHTS RESERVED</div>

</body>
</html>
```